Mexican construction company needs a business card design

We need a business card design for a company based in Monterrey, Mexico called:

Desarrollos Tolvani S.A. de C.V.

The company is in the construction business and I would like the businees card to be simple and concise. Please use white background and blue or black text color that say:

"Proyectos de Construcción"-- (Brief description of business)
" Rodrigo Ulloa Benítez"--- (My name)
"rulloab@correovelo.mx"-- (My email)
"C: (81) 82 19 57 46"-- (My cell)
"O: (81) 86 72 13 95"-- (Office phone)

Please use only the colors of my company that are attached

Please make the back of the business card blue (same blue from logo) and use the logo.

Thanks!

```html
<!DOCTYPE html>
<html lang="es">
<head>
<meta charset="utf-8">
<title>Desarrollos Tolvani – Tarjeta de presentación</title>
<link rel="stylesheet" href="https://fonts.googleapis.com/css2?family=Arimo:ital@0;1&family=Carlito:ital,wght@0,400;0,700;1,700&display=swap">
<style>
  :root {
    --navy: #211a36;
    --grey: #8c8c8c;
    --white: #ffffff;
    --ink: #000000;
    --shadow: rgba(0, 0, 0, 0.28);
  }
  html, body {
    margin: 0;
    padding: 0;
    overflow: hidden;
  }
  .sheet {
    position: relative;
    width: 849px;
    height: 1200px;
    background: var(--white);
    overflow: hidden;
    font-family: "Arimo", Arial, sans-serif;
    color: var(--ink);
  }
  .sheet-title {
    position: absolute;
    top: 98px;
    left: 0;
    width: 100%;
    margin: 0;
    text-align: center;
    font-weight: 400;
    font-size: 39px;
  }
  .side-label {
    position: absolute;
    left: 0;
    width: 100%;
    margin: 0;
    text-align: center;
    font-style: italic;
    font-weight: 400;
    font-size: 40px;
  }
  .side-label--front { top: 222px; }
  .side-label--back { top: 686px; }

  .card {
    position: absolute;
    width: 360px;
    height: 206px;
    box-shadow: 8px 10px 14px var(--shadow);
    font-family: "Carlito", Calibri, sans-serif;
    overflow: hidden;
  }
  .card--front { left: 232px; top: 331px; background: var(--white); }
  .card--back { left: 231px; top: 796px; background: var(--navy); }

  .brand {
    position: absolute;
    display: flex;
    align-items: center;
    gap: 12px;
  }
  .brand-mark {
    flex: none;
    background: var(--grey);
  }
  .brand-name {
    text-transform: uppercase;
    font-weight: 400;
    line-height: 1;
    letter-spacing: 1.5px;
  }
  .brand-name span { display: block; }
  .brand-name .brand-line-small { font-size: 12px; margin-bottom: 3px; }

  .card--front .brand { left: 20px; top: 20px; }
  .card--front .brand-mark { width: 52px; height: 52px; }
  .card--front .brand-name { color: var(--navy); font-size: 22px; }

  .card--back .brand { left: 36px; top: 68px; gap: 16px; }
  .card--back .brand-mark { width: 66px; height: 66px; }
  .card--back .brand-name { color: var(--white); font-size: 27px; }
  .card--back .brand-name .brand-line-small { font-size: 15px; }

  .tagline {
    position: absolute;
    left: 96px;
    top: 91px;
    margin: 0;
    font-weight: 700;
    font-style: italic;
    font-size: 17px;
    color: var(--navy);
  }
  .contact {
    position: absolute;
    margin: 0;
    font-size: 9px;
    color: var(--ink);
    line-height: 1;
  }
  .contact--name { left: 41px; top: 143px; }
  .contact--email { left: 234px; top: 143px; }
  .contact--cell { left: 234px; top: 162px; }
  .contact--office { left: 234px; top: 178px; }

  .card-lines {
    position: absolute;
    inset: 0;
    width: 100%;
    height: 100%;
  }
  .card-lines line {
    stroke: var(--navy);
    stroke-width: 2.6;
  }
</style>
</head>
<body>
<main class="sheet">
  <h1 class="sheet-title">Preview Business Card</h1>

  <h2 class="side-label side-label--front">Front</h2>
  <section class="card card--front" aria-label="Frente de la tarjeta">
    <svg class="card-lines" viewBox="0 0 360 206" aria-hidden="true">
      <line x1="0" y1="154" x2="167" y2="207"/>
      <line x1="361" y1="140" x2="305" y2="207"/>
    </svg>
    <div class="brand">
      <div class="brand-mark" aria-hidden="true"></div>
      <p class="brand-name"><span class="brand-line-small">Desarrollos</span><span>Tolvani</span></p>
    </div>
    <p class="tagline">Proyectos de Construcción</p>
    <p class="contact contact--name">Rodrigo Ulloa Benítez</p>
    <p class="contact contact--email">rulloab@correovelo.mx</p>
    <p class="contact contact--cell">C: (81) 82 19 57 46</p>
    <p class="contact contact--office">O: (81) 86 72 13 95</p>
  </section>

  <h2 class="side-label side-label--back">Back</h2>
  <section class="card card--back" aria-label="Reverso de la tarjeta">
    <div class="brand">
      <div class="brand-mark" aria-hidden="true"></div>
      <p class="brand-name"><span class="brand-line-small">Desarrollos</span><span>Tolvani</span></p>
    </div>
  </section>
</main>
</body>
</html>
```